Business card design Needed for new logo / Construction business, home extensions and new builds

We need a business card design using our new logo files which i will attach to this project :)

We are a small construction business specialising in home extensions, new builds and property development. We are very ambitious and would appreciate professional and elegant designs for our new business card.

Very serious about using the services on BriefNest and recently acquired our new logo from here :)

Please get involved, i will feedback when i can as i am very busy but can respond daily, thanks

Target Market(s)

People that want to build onto their houses, new building developments or adding too their existing property

Industry/Entity Type

Construction

Contact Information for Business Card

Hollin Marsh Construction, Tobias Renwick (Managing Director), Tel 07822200444, email - info@hollin-marsh, www.hollin-marsh.co.uk

Colors

Designer to choose colors to be used in the design.

Requirements
Must have
• I like a deep grey on the back please. A lot of you have provided black from and back, try mixing things up a little. The black looks cool 😎 Thanks

```html
<!DOCTYPE html>
<html lang="en">
<head>
<meta charset="utf-8">
<title>Hollin Marsh Construction – Business Card</title>
<link href="https://fonts.googleapis.com/css2?family=Cinzel:wght@600&family=Montserrat:wght@400;600&display=swap" rel="stylesheet">
<style>
  :root {
    --page: #d6d6d6;
    --paper: #ffffff;
    --ink: #2b2b2b;
    --gold: #c9962a;
    --gold-light: #ecc35c;
    --gold-dark: #a87617;
    --deep-grey: #2c2d2f;
    --rule: #9a9a9a;
  }
  * { margin: 0; padding: 0; box-sizing: border-box; }
  html, body { width: 1200px; height: 1200px; overflow: hidden; }
  body {
    background: var(--page);
    font-family: "Montserrat", sans-serif;
    display: flex;
    flex-direction: column;
    align-items: center;
    justify-content: center;
    gap: 56px;
  }
  .card {
    position: relative;
    width: 860px;
    height: 491px;
    border-radius: 34px;
    overflow: hidden;
    box-shadow: 0 10px 30px rgba(0, 0, 0, 0.18);
  }
  .card--front { background: var(--paper); }
  .card--back { background: var(--deep-grey); }

  .brand {
    position: absolute;
    left: 0; right: 0;
    display: flex;
    flex-direction: column;
    align-items: center;
    font-family: "Cinzel", serif;
    font-weight: 600;
    color: var(--gold);
    text-align: center;
    letter-spacing: 2px;
  }
  .brand__mark {
    width: 34px; height: 34px;
    background: var(--gold);
    margin-bottom: 18px;
  }
  .card--front .brand { top: 70px; font-size: 34px; line-height: 1.2; }
  .card--back .brand { top: 150px; font-size: 48px; line-height: 1.2; }
  .card--back .brand__mark { width: 46px; height: 46px; margin-bottom: 26px; }

  .person {
    position: absolute;
    left: 70px;
    top: 318px;
    padding-left: 20px;
    border-left: 8px solid var(--gold);
  }
  .person__name {
    font-weight: 600;
    font-size: 26px;
    color: var(--gold);
    letter-spacing: 0.5px;
  }
  .person__role {
    font-size: 17px;
    color: var(--ink);
    letter-spacing: 1px;
    margin-top: 2px;
  }
  .divider {
    position: absolute;
    left: 470px;
    top: 290px;
    width: 1px;
    height: 100px;
    background: var(--rule);
  }
  .contact {
    position: absolute;
    left: 500px;
    top: 290px;
    list-style: none;
    font-size: 17px;
    color: var(--ink);
  }
  .contact li {
    display: flex;
    align-items: center;
    gap: 12px;
    height: 33px;
  }
  .contact svg { width: 22px; height: 22px; flex: none; }

  .band--gold {
    position: absolute;
    left: 0; bottom: 0;
    width: 62%;
    height: 32px;
    background: linear-gradient(90deg, var(--gold-dark), var(--gold-light) 55%, var(--gold));
  }
  .band--dark {
    position: absolute;
    right: 0; bottom: 0;
    width: 37%;
    height: 44px;
    background: var(--deep-grey);
  }
</style>
</head>
<body>
  <section class="card card--front">
    <div class="brand">
      <span class="brand__mark"></span>
      <span>Hollin Marsh</span>
      <span>Construction</span>
    </div>

    <div class="person">
      <p class="person__name">TOBIAS RENWICK</p>
      <p class="person__role">MANAGING DIRECTOR</p>
    </div>

    <div class="divider"></div>

    <ul class="contact">
      <li>
        <svg viewBox="0 0 24 24" aria-hidden="true"><path fill="#c9962a" d="M6.6 10.8a15.1 15.1 0 0 0 6.6 6.6l2.2-2.2c.3-.3.7-.4 1-.2 1.1.4 2.3.6 3.6.6.6 0 1 .4 1 1V20c0 .6-.4 1-1 1A17 17 0 0 1 3 4c0-.6.4-1 1-1h3.5c.6 0 1 .4 1 1 0 1.3.2 2.5.6 3.6.1.3 0 .7-.2 1z"/></svg>
        <span>+44 7822 200 444</span>
      </li>
      <li>
        <svg viewBox="0 0 24 24" aria-hidden="true"><rect x="2" y="5" width="20" height="14" rx="1.5" fill="#c9962a"/><path d="M2.5 5.5 12 13l9.5-7.5" fill="none" stroke="#fff" stroke-width="1.6"/></svg>
        <span>info@hollin-marsh.co.uk</span>
      </li>
      <li>
        <svg viewBox="0 0 24 24" aria-hidden="true"><g fill="none" stroke="#c9962a" stroke-width="1.6"><circle cx="12" cy="12" r="9.5"/><ellipse cx="12" cy="12" rx="4" ry="9.5"/><path d="M2.5 12h19M4 7h16M4 17h16"/></g></svg>
        <span>www.hollin-marsh.co.uk</span>
      </li>
    </ul>

    <div class="band--gold"></div>
    <div class="band--dark"></div>
  </section>

  <section class="card card--back">
    <div class="brand">
      <span class="brand__mark"></span>
      <span>Hollin Marsh</span>
      <span>Construction</span>
    </div>
  </section>
</body>
</html>
```